Vitalquorra.com

I need a web design for a Online Wellness Center based in Chicago, IL and it's called "Vitalquorra" We provide Health risk assessment to individuals and interventions. Our portal has a Health Activity tracker where our members record health activities and aerobic miles and biometric data. Our Online wellness center tracks the participant's progress toward health goals and awards points for completed activities.
I started working on this website but the designer was not able to designer a website which describes what we do. I need a fresh look on this project. I need a very attractive, responsive website which says what we do.
These are the things we do.
1. We provide Health Risk Assessments to individuals and Co-operations
2. We Provide Free health screenings to undeserved communities
3. Assist individuals access free or affordable medications
4. We ask providers/doctors to see (or do a complete physical) one individual free of charge once a year (those individuals who are no insured and don't have money to pay from their pocket)
5. Assist patient access lab work at low cost
Our goal is to provide services that will lower the cost of care for our members.

Here is the website: www.vitalquorra.com still underdevelopment. PLEASE DO NOT COPY THIS STYLE OF WEBSITE. IT'S A BAD DESIGN AND THAT IS WHY I'M RE-DESIGNING THE SITE

Target Market(s)

Health individuals between the age of 21 to 65 Plus years old. Insured and uninsured

Industry/Entity Type

Health And Wellness

Coding

Coded - Design and coding required

Number of Pages Required

5+ page

Colors
0292cd

Requirements
Must have
• I'm still working on this websiteHere is the menu: Home, About us, Services, Health Screening, Providers, Contacts
• Please see. www.vitalquorra.com
Nice to have
• Event calender
• Upcoming Event
• Medication
• Lab assist
• Providers/Free Clinics

```html
<!DOCTYPE html>
<html lang="en">
<head>
<meta charset="utf-8">
<title>Vitalquorra – Online Wellness Center</title>
<link href="https://fonts.googleapis.com/css2?family=Open+Sans:wght@400;600;700&display=swap" rel="stylesheet">
<style>
:root{
  --blue:#0292cd;
  --blue-dark:#0270a0;
  --nav:#3b3b3b;
  --ink:#333;
  --muted:#666;
  --panel:#f1f1f1;
  --orange:#f0761f;
  --footer:#2b2b2b;
  --footer-bar:#1e1e1e;
}
*{box-sizing:border-box;margin:0;padding:0}
html,body{width:1200px;height:2392px;overflow:hidden}
body{font-family:"Open Sans",Arial,sans-serif;color:var(--ink);background:linear-gradient(180deg,#b8b8b8 0,#8f8f8f 600px,#9a9a9a 100%);position:relative}
.page{position:absolute;left:248px;top:0;width:696px;height:2392px;background:#fff}
.page > *{position:absolute;left:0;width:696px}
a{color:inherit;text-decoration:none}

/* header */
.topbar{top:0;height:60px;background:linear-gradient(#f4f4f4,#dcdcdc);display:flex;align-items:center;justify-content:space-between;padding:0 14px}
.brand{display:flex;align-items:center;gap:8px;font-weight:700;font-size:20px;color:var(--blue)}
.brand-dot{width:20px;height:20px;border-radius:50%;background:var(--blue)}
.account{display:flex;gap:6px;align-items:center}
.btn-sm{font-size:9px;font-weight:700;color:#fff;padding:4px 9px;border-radius:2px;background:#555}
.btn-sm.signup{background:var(--blue)}
.search-mini{width:90px;height:20px;border:1px solid #bbb;background:#fff;font-size:9px;color:#999;padding:3px 6px}
.nav{top:60px;height:60px;background:var(--nav);display:flex;align-items:center}
.nav a{color:#fff;font-size:13px;padding:0 19px;height:60px;line-height:60px}
.nav a.active{background:var(--blue)}

/* hero */
.hero{top:120px;height:472px;display:flex}
.hero-panel{width:296px;background:var(--blue);padding:30px 20px;color:#fff}
.hero-list{list-style:none}
.hero-list li{display:flex;align-items:center;gap:12px;font-size:12px;height:46px}
.hero-list .ico{width:26px;height:26px;border-radius:50%;background:#fff;display:flex;align-items:center;justify-content:center}
.hero-list .ico svg{width:14px;height:14px}
.clinic-search{margin-top:60px}
.clinic-search h4{font-size:12px;font-weight:700;margin-bottom:8px}
.clinic-search .field{width:220px;height:24px;background:#fff;font-size:10px;color:#999;padding:5px 8px}
.clinic-search .go{display:inline-block;margin-top:10px;background:var(--blue-dark);border:1px solid #fff;font-size:11px;font-weight:700;padding:4px 18px}
.hero-photo{flex:1;background:linear-gradient(135deg,#e9eef2,#c8d6df 50%,#8fa7b8)}

/* about */
.about{top:592px;height:408px;text-align:center;padding:60px 60px 0}
h2{font-weight:400;font-size:32px;color:#333}
.about p{font-size:12px;line-height:18px;color:var(--muted);margin-top:14px}
.btn{display:inline-block;background:var(--blue);color:#fff;font-size:13px;padding:8px 22px;border-radius:2px}
.about .btn{margin-top:20px}

/* services */
.services{top:1000px;height:310px;text-align:center}
.cards{display:flex;justify-content:center;gap:12px;margin-top:22px}
.card{width:200px;height:190px;background:#fff;border:1px solid #e2e2e2;padding:14px 16px;text-align:center}
.card .circle{width:58px;height:58px;border-radius:50%;border:3px solid var(--blue);background:#fff;margin:0 auto;display:flex;align-items:center;justify-content:center}
.card h3{font-weight:400;font-size:15px;margin-top:10px;color:#333}
.card p{font-size:10px;line-height:14px;color:var(--muted);margin-top:8px}
.card .more{display:inline-block;margin-top:10px;background:var(--blue);color:#fff;font-size:9px;font-weight:700;padding:4px 14px}
.card.featured{background:var(--blue);border-color:var(--blue);height:210px;margin-top:-10px}
.card.featured h3,.card.featured p{color:#fff}
.card.featured .more{background:var(--blue-dark)}
.arrow{position:absolute;top:160px;font-size:16px;color:#999}
.arrow.l{left:8px}.arrow.r{right:8px}

/* band */
.band{top:1310px;height:310px;background:linear-gradient(90deg,#3e3e3e,#5a5a5a 60%,#494949);text-align:center;color:#fff;padding-top:90px}
.band h2{color:#fff;font-size:34px;line-height:44px}
.band .btn{background:var(--orange);margin-top:16px;padding:8px 26px}

/* news & calendar */
.lower{top:1620px;height:500px;background:var(--panel)}
.news{position:absolute;left:0;top:20px;width:372px}
.sched{position:absolute;left:384px;top:20px;width:312px}
.box-head{height:40px;background:var(--blue);color:#fff;font-size:14px;line-height:40px;padding-left:14px;position:relative}
.box-head .nav-arrows{position:absolute;right:8px;top:0;font-size:11px}
.news-item{display:flex;gap:12px;padding:22px 12px 14px}
.news-thumb{width:110px;height:80px;flex:none;background:linear-gradient(135deg,#dfe7ec,#a9bccb)}
.news-meta{font-size:11px;color:var(--blue);font-weight:600}
.news-item p{font-size:10px;line-height:14px;color:var(--muted);margin-top:4px}
.news-item .rm{font-size:10px;font-weight:700;color:#333;margin-top:4px;display:block}
.cal{margin:18px auto 0;width:250px;background:#fff;border:1px solid #ccc}
.cal-head{background:#ddd;text-align:center;font-size:13px;letter-spacing:2px;padding:8px 0;color:#444}
.cal table{width:100%;border-collapse:collapse}
.cal td{height:32px;text-align:center;font-size:10px;color:#555;border:1px solid #e1e1e1;background:#eaeaea}
.cal td.day{background:#ccc;font-weight:700;height:22px}
.cal td.on{background:var(--blue);color:#fff}
.sched .btn{display:block;width:140px;margin:16px auto 0;font-size:10px;font-weight:700;text-align:center;padding:6px 0}

/* footer */
.footer{top:2130px;height:230px;background:var(--footer);color:#ccc;display:flex;padding:24px 18px;gap:20px}
.fcol{flex:1;font-size:10px}
.fcol h5{font-size:12px;color:#fff;font-weight:600;margin-bottom:12px}
.fcol li{list-style:none;margin-bottom:8px;padding-left:10px;position:relative}
.fcol li::before{content:"";position:absolute;left:0;top:5px;width:4px;height:4px;background:var(--blue)}
.fcol .line{margin-bottom:10px;line-height:14px}
.social{display:flex;gap:6px;margin-top:6px}
.social span{width:18px;height:18px;border-radius:50%;background:#555}
.qc .input{display:block;width:100%;height:20px;background:#444;margin-bottom:6px;font-size:9px;color:#999;padding:4px 6px}
.qc .ta{height:38px}
.qc .send{display:inline-block;background:var(--blue);color:#fff;font-size:9px;padding:4px 12px}
.footer-bar{top:2360px;height:32px;background:var(--footer-bar);color:#888;font-size:9px;line-height:32px;padding-left:18px}
</style>
</head>
<body>
<div class="page">
  <header class="topbar">
    <a class="brand" href="#"><span class="brand-dot"></span>Vitalquorra</a>
    <div class="account">
      <span class="btn-sm">LOGIN</span>
      <span class="btn-sm signup">SIGN UP</span>
      <span class="search-mini">Search</span>
    </div>
  </header>
  <nav class="nav">
    <a class="active" href="#">Home</a><a href="#">About Us</a><a href="#">Our Service</a><a href="#">Health Screening</a><a href="#">Provider</a><a href="#">Contact</a>
  </nav>

  <section class="hero">
    <div class="hero-panel">
      <ul class="hero-list">
        <li><span class="ico"><svg viewBox="0 0 14 14"><path d="M2 7l3 3 7-7" stroke="#0292cd" stroke-width="2" fill="none"/></svg></span>Health Risk Assessments</li>
        <li><span class="ico"><svg viewBox="0 0 14 14"><path d="M5 1h4v4h4v4H9v4H5V9H1V5h4z" fill="#0292cd"/></svg></span>Free health screenings</li>
        <li><span class="ico"><svg viewBox="0 0 14 14"><rect x="1" y="4" width="12" height="6" rx="3" fill="#0292cd"/></svg></span>Free medications</li>
        <li><span class="ico"><svg viewBox="0 0 14 14"><circle cx="7" cy="4" r="3" fill="#0292cd"/><path d="M1 13c0-4 12-4 12 0z" fill="#0292cd"/></svg></span>Doctors</li>
        <li><span class="ico"><svg viewBox="0 0 14 14"><path d="M5 1h4v5l3 6H2l3-6z" fill="#0292cd"/></svg></span>Access lab work</li>
      </ul>
      <div class="clinic-search">
        <h4>Free and Partial Clinics in Illinois</h4>
        <div class="field">Enter your zipcode</div>
        <span class="go">SEARCH</span>
      </div>
    </div>
    <div class="hero-photo" role="img" aria-label="Photo of a lab technician working with test tubes"></div>
  </section>

  <section class="about">
    <h2>About Us</h2>
    <p>Lorem Ipsum is simply dummy text of the printing and typesetting industry. Lorem Ipsum has been the industry's standard dummy text ever since the 1500s, when an unknown printer took a galley of type and scrambled it to make a type specimen book. It has survived not only five centuries, but also the leap into electronic typesetting, remaining essentially unchanged. It was popularised.</p>
    <a class="btn" href="#">Read More</a>
  </section>

  <section class="services">
    <h2>Service</h2>
    <span class="arrow l">&#8249;</span><span class="arrow r">&#8250;</span>
    <div class="cards">
      <div class="card">
        <div class="circle"><svg width="28" height="28" viewBox="0 0 28 28"><path d="M10 2h8v8h8v8h-8v8h-8v-8H2v-8h8z" fill="#0292cd"/></svg></div>
        <h3>Emergency Care</h3>
        <p>Contrary to popular belief, Lorem Ipsum is not simply random text. It has roots in a piece.</p>
        <span class="more">MORE</span>
      </div>
      <div class="card featured">
        <div class="circle"><svg width="28" height="28" viewBox="0 0 28 28"><rect x="3" y="9" width="22" height="10" rx="5" fill="#0292cd"/></svg></div>
        <h3>Medication</h3>
        <p>Contrary to popular belief, Lorem Ipsum is not simply random text. It has roots in a piece.</p>
        <span class="more">MORE</span>
      </div>
      <div class="card">
        <div class="circle"><svg width="28" height="28" viewBox="0 0 28 28"><path d="M10 3h8v9l6 12H4l6-12z" fill="#0292cd"/></svg></div>
        <h3>Lab work at low cost</h3>
        <p>Contrary to popular belief, Lorem Ipsum is not simply random text. It has roots in a piece.</p>
        <span class="more">MORE</span>
      </div>
    </div>
  </section>

  <section class="band" role="img" aria-label="Darkened photo of a doctor with a patient behind the message">
    <h2>We Provide Free health screenings to<br>underserved communities</h2>
    <a class="btn" href="#">Know More</a>
  </section>

  <section class="lower">
    <div class="news">
      <div class="box-head">Latest News<span class="nav-arrows">&#9664; &#9654;</span></div>
      <div class="news-item">
        <div class="news-thumb" role="img" aria-label="News photo of a doctor"></div>
        <div>
          <div class="news-meta">05 JAN 2015 &nbsp; 4</div>
          <p>It is a long established fact that a reader will be distracted by the readable content of a page.</p>
          <span class="rm">Read More</span>
        </div>
      </div>
      <div class="news-item">
        <div class="news-thumb" role="img" aria-label="News photo of medical staff"></div>
        <div>
          <div class="news-meta">05 JAN 2015 &nbsp; 4</div>
          <p>It is a long established fact that a reader will be distracted by the readable content of a page.</p>
          <span class="rm">Read More</span>
        </div>
      </div>
    </div>
    <div class="sched">
      <div class="box-head">Our Screening Schedule<span class="nav-arrows">&#9664; &#9654;</span></div>
      <div class="cal">
        <div class="cal-head">OCTOBER</div>
        <table>
          <tr><td class="day">Sun</td><td class="day">Mon</td><td class="day">Tue</td><td class="day">Wed</td><td class="day">Thu</td><td class="day">Fri</td><td class="day">Sat</td></tr>
          <tr><td></td><td></td><td></td><td>1</td><td>2</td><td>3</td><td>4</td></tr>
          <tr><td>5</td><td>6</td><td>7</td><td>8</td><td>9</td><td>10</td><td>11</td></tr>
          <tr><td>12</td><td>13</td><td>14</td><td class="on">15</td><td>16</td><td>17</td><td>18</td></tr>
          <tr><td>19</td><td>20</td><td>21</td><td>22</td><td class="on">23</td><td>24</td><td>25</td></tr>
          <tr><td>26</td><td>27</td><td>28</td><td>29</td><td>30</td><td>31</td><td></td></tr>
        </table>
      </div>
      <a class="btn" href="#">CHECK YOUR EVENT</a>
    </div>
  </section>

  <footer class="footer">
    <div class="fcol">
      <h5>Main menu</h5>
      <ul><li>Home</li><li>About Us</li><li>Service</li><li>Blog</li><li>Contact</li></ul>
    </div>
    <div class="fcol">
      <h5>Information</h5>
      <ul><li>Partners</li><li>Legal Notice</li><li>Terms and conditions of use</li><li>Benefits of members</li><li>Contact</li></ul>
    </div>
    <div class="fcol">
      <h5>Contact us</h5>
      <div class="line">Vitalquorra<br>218 Larkmoor Avenue<br>Brookfield Heights, IL 62719</div>
      <div class="line">(555) 014-2270</div>
      <div class="line">info@vitalquorra.com</div>
      <div class="social"><span></span><span></span><span></span></div>
    </div>
    <div class="fcol qc">
      <h5>Quick Contact</h5>
      <div class="line">Leave your message</div>
      <div class="input">Your Name</div>
      <div class="input">Email Address</div>
      <div class="input ta">Message</div>
      <span class="send">Submit</span>
    </div>
  </footer>
  <div class="footer-bar">Vitalquorra.com 2015. All rights reserved.</div>
</div>
</body>
</html>
```